QUORVA Fiesta 2013 - Urban & Extreme Sports Festival

***Who we are and what we are doing***
We are organizing an urban and extreme sports festival in summer. This is our first year, and so far things are progressing nicely.
The QUORVA Fiesta is an event that caters to not only the athletes but the general public as well.
Each of these events will have three key-elements; an exhibition, a workshop and a competition element. The aim is to not only showcase the various sports and their participants, but more importantly to give those interested, the opportunity to try something new.
We will have the following sports; BMX, Inline skate, Skateboard, Scooter. Circus Skills will also be a major feature (juggling, poi, devil sticks etc), as well as Street Art demonstrations.
There will be hog roasts and barbecues all weekend, as well as live bands and DJs.
We are expecting a broad range of ages attending, and are trying to appeal to families also. But most of the active participants will be between the ages of 15-30
***What we would like***
We are looking for a website template that we can then fill out with all the information ourselves.
The website must have a clean, fresh, summery, urban feel.
We will need to following buttons along the top,
About / Schedule / Partners / Media / Registration / Venue / Contact
We would also like the dates to be clear (24th 25th 26th August 2013) somewhere.
And we would like to say a huge thank you in advance to all the designers.
Looking forward to seeing what you all come up with.
Any questions please get in touch and we will do our best to answer as soon as possible!
Dunn.
Young active adventurous sporty urban cool people
Festival

```html
<!DOCTYPE html>
<html lang="en">
<head>
<meta charset="utf-8">
<title>QUORVA Fiesta 2013</title>
<link href="https://fonts.googleapis.com/css2?family=Roboto+Condensed:wght@400;700&family=PT+Sans:wght@400;700&display=swap" rel="stylesheet">
<style>
:root{
  --wood-dark:#242424;
  --wood-mid:#343434;
  --white:#ffffff;
  --ink:#2b2b2b;
  --body-ink:#3a2f2a;
  --chip:#2a2a2a;
  --rule:#dcdcdc;
  --grey-btn:#8a8a8a;
  --brand-grey:#b4b4b4;
}
*{margin:0;padding:0;box-sizing:border-box}
html,body{width:1049px;height:1200px;overflow:hidden;background:var(--white)}
body{position:relative;font-family:"PT Sans",sans-serif;color:var(--ink)}
.abs{position:absolute}
.wood{background:
  repeating-linear-gradient(90deg,rgba(255,255,255,.025) 0 2px,rgba(0,0,0,.04) 2px 5px,rgba(255,255,255,.015) 5px 9px),
  linear-gradient(90deg,var(--wood-dark),var(--wood-mid) 30%,var(--wood-dark) 55%,var(--wood-mid) 80%,var(--wood-dark))}
.cond{font-family:"Roboto Condensed",sans-serif;font-weight:700}

.site-header{left:0;top:0;width:1049px;height:134px}
.brand{left:66px;top:46px;display:flex;align-items:center;gap:10px;color:var(--brand-grey);font-size:27px;letter-spacing:.5px}
.brand-mark{width:24px;height:24px;border-radius:50%;background:var(--brand-grey)}
.main-nav{left:309px;top:68px;display:flex;gap:27px;color:var(--white);font-size:16px;font-weight:400;letter-spacing:.2px}

.hero-frame{left:74px;top:148px;width:900px;height:341px;background:var(--white);box-shadow:0 8px 12px rgba(0,0,0,.25);border:1px solid #e6e6e6}
.hero-photo{left:6px;top:6px;width:888px;height:329px;overflow:hidden;
  background:
   radial-gradient(ellipse 260px 90px at 630px 300px,rgba(170,210,245,.85),rgba(170,210,245,0)),
   linear-gradient(180deg,#0d4aa8 0%,#2d7bd8 55%,#4a9ae8 76%,#1f5fb8 82%,#2b6cc4 100%)}
.hero-arrow{top:156px}
.hero-title{left:21px;top:270px;color:var(--white);font-size:22px;text-shadow:0 1px 2px rgba(0,0,0,.35)}
.hero-sub{left:21px;top:298px;color:var(--white);font-size:12px}
.sched-label{left:500px;top:281px;color:#141414;font-size:19px}
.sched-dates{left:646px;top:268px;width:229px;height:44px;background:var(--chip);color:var(--white);font-size:17px;font-weight:400;display:flex;align-items:center;justify-content:center}

.games{left:0;top:510px;width:1049px;height:222px}
.games-title{left:78px;top:16px;color:var(--white);font-size:21px}
.game-card{top:50px;width:212px;height:151px;border:3px solid var(--white);background:#2b2b2b}
.game-photo{left:0;top:0;width:206px;height:110px}
.game-label{left:13px;top:116px;color:var(--white);font-size:19px}

.partners-title{left:0;top:743px;width:1049px;text-align:center;font-size:20px;color:#222}
.rule{top:757px;height:1px;background:var(--rule)}
.p-arrow{top:795px;width:26px;height:26px;border-radius:50%;background:var(--grey-btn)}
.partner{top:796px;font-size:18px;color:#222;transform:translateX(-50%);white-space:nowrap}

.welcome-title{left:80px;top:866px;font-size:26px;color:#222}
.welcome-lead{left:80px;top:904px;font-size:16px;color:#222}
.welcome-text{left:80px;top:930px;width:545px;font-size:11px;line-height:19.5px;color:var(--body-ink)}
.welcome-text p+p{margin-top:13px}
.read-more{left:78px;top:1047px;width:85px;height:30px;background:#1f1f1f;color:var(--white);border-radius:3px;font-size:14px;display:flex;align-items:center;justify-content:center}

.video-frame{left:652px;top:864px;width:311px;height:192px;background:var(--white);border:1px solid #e3e3e3;box-shadow:0 2px 6px rgba(0,0,0,.15)}
.video-still{left:4px;top:4px;width:302px;height:184px;
  background:linear-gradient(165deg,#2f6dcf 0%,#7fa9dc 35%,#b9c7d6 55%,#eef2f6 72%,#d6dde6 100%)}
.play{left:127px;top:66px}
.progress{left:6px;top:171px;width:272px;height:2px;background:rgba(255,255,255,.75)}

.site-footer{left:0;top:1091px;width:1049px;height:109px}
.foot-nav{left:80px;top:33px;color:var(--white);font-size:13px;font-weight:400}
.copyright{left:80px;top:63px;color:#c8c8c8;font-size:10px}
.social{top:26px;display:flex;gap:4px}
.social span{width:28px;height:28px;border-radius:50%;background:var(--white);display:block}
</style>
</head>
<body>

<header class="abs site-header wood">
  <div class="abs brand cond"><span class="brand-mark"></span>QUORVA Fiesta</div>
  <nav class="abs main-nav cond">
    <span>HOME</span><span>ABOUT</span><span>SCHEDULE</span><span>PARTNERS</span><span>MEDIA</span><span>REGISTRATION</span><span>VENUE</span><span>CONTACT</span>
  </nav>
</header>

<section class="abs hero-frame">
  <div class="abs hero-photo" role="img" aria-label="Freestyle skier jumping against a blue sky with falling snow above the sea">
    <svg class="abs hero-arrow" style="left:12px" width="16" height="30" viewBox="0 0 16 30"><path d="M14 2 L2 15 L14 28" fill="none" stroke="#fff" stroke-width="2"/></svg>
    <svg class="abs hero-arrow" style="left:860px" width="16" height="30" viewBox="0 0 16 30"><path d="M2 2 L14 15 L2 28" fill="none" stroke="#fff" stroke-width="2"/></svg>
    <div class="abs hero-title cond">MAECENAS ALIQUET VELIT</div>
    <div class="abs hero-sub">MAURIS NEQUE METUS, MALESUADA NEC ULTRICIES</div>
    <div class="abs sched-label cond">SCHEDULE DATES</div>
    <div class="abs sched-dates cond">24th 25th 26th August 2013</div>
  </div>
</section>

<section class="abs games wood">
  <h2 class="abs games-title cond">OUR GAMES</h2>
  <div class="abs game-card" style="left:74px">
    <div class="abs game-photo" role="img" aria-label="Group of inline skaters racing on a road" style="background:linear-gradient(180deg,#4d6b3c 0%,#7d8f6a 30%,#6f7fa8 60%,#c8b7a8 100%)"></div>
    <div class="abs game-label">Inline skate</div>
  </div>
  <div class="abs game-card" style="left:302px">
    <div class="abs game-photo" role="img" aria-label="BMX rider in mid-air trick" style="background:linear-gradient(180deg,#d9d8cc 0%,#b3b29c 45%,#6e7560 80%,#3f4a3e 100%)"></div>
    <div class="abs game-label">BMX</div>
  </div>
  <div class="abs game-card" style="left:532px">
    <div class="abs game-photo" role="img" aria-label="Skateboard close-up on pavement" style="background:linear-gradient(180deg,#e9dcc2 0%,#3f7aa8 30%,#1d4a70 65%,#5f8aa6 100%)"></div>
    <div class="abs game-label">Skateboard</div>
  </div>
  <div class="abs game-card" style="left:759px">
    <div class="abs game-photo" role="img" aria-label="Scooter rider jumping against the sky" style="background:linear-gradient(180deg,#9fb4c8 0%,#d6e0e8 60%,#8a8f86 82%,#3e4438 100%)"></div>
    <div class="abs game-label">Scooter</div>
  </div>
</section>

<section>
  <div class="abs rule" style="left:80px;width:392px"></div>
  <div class="abs rule" style="left:574px;width:394px"></div>
  <h2 class="abs partners-title cond">PARTNERS</h2>
  <span class="abs p-arrow" style="left:131px"><svg width="26" height="26"><path d="M15 8 L10 13 L15 18Z" fill="#fff"/></svg></span>
  <span class="abs p-arrow" style="left:867px"><svg width="26" height="26"><path d="M11 8 L16 13 L11 18Z" fill="#fff"/></svg></span>
  <span class="abs partner cond" style="left:252px">Brisk Wheels</span>
  <span class="abs partner cond" style="left:405px">rampcity</span>
  <span class="abs partner cond" style="left:570px">KORA Works</span>
  <span class="abs partner cond" style="left:660px">Vexo</span>
  <span class="abs partner cond" style="left:752px">Spindome</span>
</section>

<section>
  <h1 class="abs welcome-title cond">WELCOME TO OUR WEBSITE MAINPAGE</h1>
  <p class="abs welcome-lead">Phasellus felis dolor, scelerisque a, tempus eget, lobortis id, libero.</p>
  <div class="abs welcome-text">
    <p>Welcome to the QUORVA Fiesta website. Very soon you will be able to find everything you need to know about what we have in store. We are currently working hard to creating an event that caters to not only the athletes and players of the sports and activities that you will find at the festival but to the general public as well.</p>
    <p>This will be a multifaceted event where collectives and like minded people from each discipline will come along and showcase what it is they do best whilst encouraging the general public to watch, learn and participate.</p>
  </div>
  <div class="abs read-more cond">READ MORE</div>

  <div class="abs video-frame">
    <div class="abs video-still" role="img" aria-label="Skier carving down a snowy mountain slope under a blue sky">
      <svg class="abs play" width="50" height="50" viewBox="0 0 50 50"><circle cx="25" cy="25" r="25" fill="rgba(60,60,60,.75)"/><path d="M20 15 L34 25 L20 35Z" fill="#fff"/></svg>
      <div class="abs progress"></div>
      <svg class="abs" style="left:282px;top:167px" width="16" height="10"><path d="M0 1 L6 5 L0 9Z" fill="#fff"/><rect x="9" y="1" width="2" height="8" fill="#fff"/><rect x="13" y="1" width="2" height="8" fill="#fff"/></svg>
    </div>
  </div>
</section>

<footer class="abs site-footer wood">
  <nav class="abs foot-nav cond">HOME / ABOUT / SCHEDULE / PARTNERS / MEDIA / REGISTRATION / VENUE / CONTACT</nav>
  <p class="abs copyright">© 2013 Company Name.&nbsp; All right reserved.&nbsp; Term of Use</p>
  <div class="abs social" style="left:844px" aria-label="Social links"><span></span><span></span><span></span><span></span></div>
</footer>

</body>
</html>
```